Breezeway Comfort business cards design

Need a business card design for a Heating and Air Conditioning business. I need these items included.
Business name: Breezeway Comfort
Owner: Marcus Tollefsen
License # 2874590
Phone number # 555-382-4071
Email: breezewaycomfortair@mailvista.example
Sales
Service
Installation
Maintenance

Heating and Air Conditioning

Requirements
Must have
• Company name , license number , phone number , email

```html
<!DOCTYPE html>
<html lang="en">
<head>
<meta charset="utf-8">
<title>Breezeway Comfort – Business Cards</title>
<link href="https://fonts.googleapis.com/css2?family=Montserrat:wght@400;700&display=swap" rel="stylesheet">
<style>
  :root {
    --page-bg: #ededed;
    --card-bg: #ffffff;
    --brand-blue: #0a3ca8;
    --brand-orange: #e85424;
    --white: #ffffff;
  }
  html, body {
    margin: 0;
    padding: 0;
    width: 938px;
    height: 1200px;
    overflow: hidden;
    background: var(--page-bg);
    font-family: "Montserrat", Arial, sans-serif;
  }
  .canvas { position: relative; width: 938px; height: 1200px; }
  .card {
    position: absolute;
    left: 168px;
    width: 602px;
    height: 354px;
    background: var(--card-bg);
    overflow: hidden;
  }
  .card--front { top: 189px; }
  .card--back { top: 655px; }

  .brand {
    position: absolute;
    display: flex;
    align-items: center;
    gap: 10px;
    color: var(--brand-blue);
    font-weight: 700;
    white-space: nowrap;
  }
  .brand__dot {
    border-radius: 50%;
    background: var(--brand-orange);
    flex: none;
  }
  .card--front .brand { left: 38px; top: 156px; font-size: 22px; }
  .card--front .brand__dot { width: 26px; height: 26px; }
  .card--back .brand {
    left: 0; right: 0; top: 168px;
    justify-content: center;
    font-size: 32px;
    gap: 14px;
  }
  .card--back .brand__dot { width: 38px; height: 38px; }

  .divider {
    position: absolute;
    left: 338px;
    top: 100px;
    width: 2px;
    height: 150px;
    background: var(--brand-blue);
  }
  .person { position: absolute; left: 366px; top: 96px; }
  .person__name {
    margin: 0;
    color: var(--brand-orange);
    font-weight: 700;
    font-size: 26px;
    letter-spacing: -0.5px;
    line-height: 32px;
  }
  .person__role {
    margin: 2px 0 0 2px;
    color: var(--brand-blue);
    font-size: 17px;
    line-height: 22px;
  }
  .contact {
    position: absolute;
    left: 366px;
    display: flex;
    align-items: center;
    color: var(--brand-blue);
    font-size: 18px;
  }
  .contact svg { width: 28px; height: 28px; margin-right: 14px; }
  .contact--phone { top: 182px; }
  .contact--license { top: 220px; }

  .band { position: absolute; left: 0; top: 321px; width: 602px; height: 33px; }
  .band__email {
    position: absolute;
    left: 0; right: 0; top: 321px; height: 33px;
    display: flex;
    align-items: center;
    justify-content: center;
    gap: 14px;
    padding-left: 70px;
    color: var(--white);
    font-size: 15px;
    box-sizing: border-box;
  }
  .band__email svg { width: 24px; height: 18px; }
</style>
</head>
<body>
<div class="canvas">

  <section class="card card--front">
    <div class="brand"><span class="brand__dot"></span>Breezeway Comfort</div>

    <div class="divider"></div>

    <div class="person">
      <h1 class="person__name">Marcus Tollefsen</h1>
      <p class="person__role">Owner</p>
    </div>

    <div class="contact contact--phone">
      <svg viewBox="0 0 24 24" aria-hidden="true">
        <path fill="#e85424" d="M6.6 10.8a15.1 15.1 0 0 0 6.6 6.6l2.2-2.2a1 1 0 0 1 1-.25 11.4 11.4 0 0 0 3.6.57 1 1 0 0 1 1 1V20a1 1 0 0 1-1 1A17 17 0 0 1 3 4a1 1 0 0 1 1-1h3.5a1 1 0 0 1 1 1c0 1.25.2 2.45.57 3.57a1 1 0 0 1-.25 1z"/>
      </svg>
      <span>555-382-4071</span>
    </div>

    <div class="contact contact--license">
      <svg viewBox="0 0 24 24" aria-hidden="true">
        <rect x="3" y="1" width="14" height="19" rx="2" fill="#e85424"/>
        <rect x="6" y="5" width="8" height="1.6" fill="#fff"/>
        <rect x="6" y="8.5" width="8" height="1.6" fill="#fff"/>
        <rect x="6" y="12" width="5" height="1.6" fill="#fff"/>
        <circle cx="17.5" cy="17" r="4.5" fill="#e85424" stroke="#fff" stroke-width="1.2"/>
        <path d="M15.6 17l1.3 1.3 2.4-2.6" fill="none" stroke="#fff" stroke-width="1.3"/>
      </svg>
      <span>2874590</span>
    </div>

    <svg class="band" viewBox="0 0 602 33" aria-hidden="true">
      <polygon points="0,0 61,0 34,33 0,33" fill="#0a3ca8"/>
      <polygon points="90,0 602,0 602,33 61,33" fill="#e85424"/>
    </svg>
    <div class="band__email">
      <svg viewBox="0 0 24 18" aria-hidden="true">
        <rect x="1" y="1" width="22" height="16" rx="1.5" fill="none" stroke="#fff" stroke-width="1.6"/>
        <path d="M1.5 1.8L12 10.5 22.5 1.8M1.5 16.5l7.5-7M22.5 16.5l-7.5-7" fill="none" stroke="#fff" stroke-width="1.4"/>
      </svg>
      <span>breezewaycomfortair@mailvista.example</span>
    </div>
  </section>

  <section class="card card--back">
    <div class="brand"><span class="brand__dot"></span>Breezeway Comfort</div>
    <svg class="band" viewBox="0 0 602 33" aria-hidden="true">
      <polygon points="0,0 61,0 34,33 0,33" fill="#0a3ca8"/>
      <polygon points="90,0 602,0 602,33 61,33" fill="#e85424"/>
    </svg>
  </section>

</div>
</body>
</html>
```